Process Diagram - Circular Economy

I would like for a designer to take this rough sketch and turn it into a high quality design which can be used in a business presentation. Seeking to get both PDF and Jpeg file versions of the finished product.

Colours don't have to be the exact same as the rough sketch PDF, the green used is pretty ugly so open to some changes.

Target Market(s)

Corporate audience

Requirements
Must have
• Clear text for each party; VENOR, TORVIN, BUYER

Smaller text for the functions; marketing, recovery, logistics, cleaning, decontamination, testing & re-certification, storage, engineering suitability

```html
<!DOCTYPE html>
<html lang="en">
<head>
<meta charset="utf-8">
<title>Circular Economy Process</title>
<link rel="stylesheet" href="https://fonts.googleapis.com/css2?family=Jost:wght@500;600;700&display=swap">
<style>
  :root {
    --bg: #efefef;
    --vendor-teal: #37b9c9;
    --recovery-teal: #45b2b8;
    --buyer-lime: #d1df18;
    --accent-orange: #fd7b18;
    --logistics-sage: #88a283;
    --cleaning-tan: #b09862;
    --decon-amber: #e8ab18;
    --testing-gold: #e1bc18;
    --storage-yellow: #d8cb18;
    --engineering-lime: #d1df18;
    --label: #ffffff;
  }
  html, body {
    margin: 0;
    padding: 0;
    width: 1200px;
    height: 1000px;
    overflow: hidden;
    background: var(--bg);
  }
  .diagram {
    display: block;
    width: 1200px;
    height: 1000px;
    font-family: "Jost", "Futura", sans-serif;
  }
  .party-label {
    fill: var(--label);
    font-weight: 700;
    font-size: 42px;
    letter-spacing: 1px;
  }
  .hub-label {
    fill: var(--label);
    font-weight: 700;
    font-size: 38px;
    letter-spacing: 1px;
  }
  .step-label {
    fill: var(--label);
    font-weight: 600;
    font-size: 15px;
    letter-spacing: 0.3px;
  }
  .step-label--centered { text-anchor: middle; }
  .buyer-arrow { fill: var(--buyer-lime); }
  .vendor-band { fill: var(--vendor-teal); }
  .marketing-strip { fill: var(--accent-orange); }
  .seg-recovery { fill: var(--recovery-teal); }
  .seg-logistics { fill: var(--logistics-sage); }
  .seg-cleaning { fill: var(--cleaning-tan); }
  .seg-hub { fill: var(--accent-orange); }
  .seg-decontamination { fill: var(--decon-amber); }
  .seg-testing { fill: var(--testing-gold); }
  .seg-storage { fill: var(--storage-yellow); }
  .seg-engineering { fill: var(--engineering-lime); }
</style>
</head>
<body>
<svg class="diagram" viewBox="0 0 1200 1000" xmlns="http://www.w3.org/2000/svg" role="img" aria-label="Circular economy process from vendor through Torvin services to buyer">
  <defs>
    <filter id="soft-shadow" x="-10%" y="-10%" width="120%" height="120%">
      <feDropShadow dx="2" dy="3" stdDeviation="3" flood-color="#000" flood-opacity="0.18"/>
    </filter>
  </defs>

  <g filter="url(#soft-shadow)">
    <!-- Buyer outflow arrow -->
    <polygon class="buyer-arrow" points="600,336 987,267 986,249 1117,297 1010,387 1006,370 760,411 700,420"/>

    <!-- Service ring -->
    <g class="service-ring">
      <path class="seg-engineering" d="M391.8,528.8 A209,209 0 0 1 600,338 L600,443 A104,104 0 0 0 496.4,538 Z"/>
      <path class="seg-recovery" d="M600,338 A209,209 0 0 1 704.5,366 L652,457 A104,104 0 0 0 600,443 Z"/>
      <path class="seg-logistics" d="M704.5,366 A209,209 0 0 1 781,442.5 L690.1,495 A104,104 0 0 0 652,457 Z"/>
      <path class="seg-cleaning" d="M781,442.5 A209,209 0 0 1 809,547 L704,547 A104,104 0 0 0 690.1,495 Z"/>
      <path class="seg-hub" d="M809,547 A209,209 0 0 1 681.7,739.5 L640.7,642.8 A104,104 0 0 0 704,547 Z"/>
      <path class="seg-decontamination" d="M681.7,739.5 A209,209 0 0 1 518.3,739.5 L559.3,642.8 A104,104 0 0 0 640.7,642.8 Z"/>
      <path class="seg-testing" d="M518.3,739.5 A209,209 0 0 1 419,651.5 L509.9,599 A104,104 0 0 0 559.3,642.8 Z"/>
      <path class="seg-storage" d="M419,651.5 A209,209 0 0 1 391.8,528.8 L496.4,538 A104,104 0 0 0 509.9,599 Z"/>
    </g>

    <!-- Vendor inflow band -->
    <polygon class="vendor-band" points="83,245 600,336 600,429 83,350"/>

    <!-- Marketing strip -->
    <path class="marketing-strip" d="M297,377 L600,430 C660,440 702,478 704,547 C694,494 656,462 600,454 L297,400 Z"/>
  </g>

  <!-- Party labels -->
  <text class="party-label" x="138" y="320" transform="rotate(10 138 320)">VENDOR</text>
  <text class="party-label" x="855" y="355" transform="rotate(-9 855 355)">BUYER</text>

  <!-- Step labels -->
  <text class="step-label" x="362" y="405" transform="rotate(10 362 405)">Marketing</text>
  <text class="step-label step-label--centered" x="645" y="394" transform="rotate(-75 645 394)">Recovery</text>
  <text class="step-label step-label--centered" x="713" y="435" transform="rotate(-50 713 435)">Logistics</text>
  <text class="step-label step-label--centered" x="753" y="510" transform="rotate(-17 753 510)">Cleaning</text>
  <text class="step-label step-label--centered" x="598" y="707">Decontamination</text>
  <text class="step-label step-label--centered" x="491" y="653">Testing &amp;</text>
  <text class="step-label step-label--centered" x="491" y="671">Re-certification</text>
  <text class="step-label step-label--centered" x="446" y="584">Storage</text>
  <text class="step-label step-label--centered" x="459" y="485">Engineering</text>
  <text class="step-label step-label--centered" x="459" y="502">Suitability</text>

  <!-- Hub label -->
  <text class="hub-label" x="745" y="630" text-anchor="middle" transform="rotate(-58 745 630)">TORVIN</text>
</svg>
</body>
</html>
```